Torvane PT Business Card

I need the card to be bright/bold colours to stand out amongst others.
It needs to have my company logo.
I was not interested in pictures etc just a layout that attracts attention.

I have attached my old design which is very plain. I also needed change the contact details. And my description changed to Personal Trainer
Phone 0427391058
Facebook Torvane PT
No email address please, no street address.
And only Torvane PT (Please remove anything to do with Torvane Supplements)

```html
<!DOCTYPE html>
<html lang="en">
<head>
<meta charset="utf-8">
<title>Torvane PT Business Card</title>
<link href="https://fonts.googleapis.com/css2?family=Lato:wght@400;700;900&display=swap" rel="stylesheet">
<style>
  :root {
    --page-bg: #2b2b2b;
    --card-white: #f4f4f4;
    --card-black: #050505;
    --brand-blue: #1d7fc0;
    --brand-blue-light: #3aa3e3;
    --brand-yellow: #f2d01a;
    --ink: #111111;
  }
  * { margin: 0; padding: 0; box-sizing: border-box; }
  html, body {
    width: 1200px; height: 997px; overflow: hidden;
    background: var(--page-bg);
    font-family: "Lato", Arial, sans-serif;
  }
  .business-card {
    position: absolute; left: 150px; top: 241px;
    width: 900px; height: 515px;
    border-radius: 28px; overflow: hidden;
    background: var(--card-white);
  }
  .card-shapes { position: absolute; inset: 0; }
  .brand-name {
    position: absolute; left: 0; right: 0; top: 118px;
    text-align: center;
    font-weight: 900; font-size: 72px; letter-spacing: 2px;
    color: var(--brand-yellow);
  }
  .person { position: absolute; left: 0; right: 0; top: 246px; text-align: center; }
  .person-name {
    font-weight: 900; font-size: 30px; letter-spacing: 1px;
    color: var(--brand-yellow);
  }
  .person-title {
    font-weight: 700; font-size: 17px; color: var(--ink); margin-top: 2px;
  }
  .contact-list { position: absolute; left: 36px; top: 392px; list-style: none; }
  .contact-item {
    display: flex; align-items: center; gap: 16px;
    height: 40px; margin-bottom: 6px;
    font-weight: 700; font-size: 25px; color: var(--brand-yellow);
  }
  .contact-icon { width: 32px; height: 32px; flex: none; }
</style>
</head>
<body>
  <div class="business-card">
    <svg class="card-shapes" viewBox="0 0 900 515" width="900" height="515" aria-hidden="true">
      <line x1="250" y1="212" x2="650" y2="212" stroke="var(--brand-blue)" stroke-width="2"/>
      <polygon points="0,300 205,300 245,228 655,228 695,300 900,300 900,314 0,314" fill="var(--brand-blue-light)"/>
      <polygon points="218,314 255,238 645,238 682,314" fill="var(--brand-blue)"/>
      <rect x="0" y="314" width="900" height="201" fill="var(--card-black)"/>
    </svg>

    <div class="brand-name">TORVANE PT</div>

    <div class="person">
      <div class="person-name">DANA MARSH</div>
      <div class="person-title">Personal Trainer</div>
    </div>

    <ul class="contact-list">
      <li class="contact-item">
        <svg class="contact-icon" viewBox="0 0 32 32" aria-hidden="true">
          <circle cx="16" cy="16" r="16" fill="var(--brand-blue)"/>
          <path d="M11 9c1 0 2 3 2 4s-1.5 1.5-1 2.5c1 2 3 4 4.5 4.5 1 .5 1.5-1 2.5-1s4 1 4 2-1.5 3-3 3C14 24 8 18 8 12c0-1.5 2-3 3-3z" fill="#fff"/>
        </svg>
        <span>0427391058</span>
      </li>
      <li class="contact-item">
        <svg class="contact-icon" viewBox="0 0 32 32" aria-hidden="true">
          <circle cx="16" cy="16" r="16" fill="var(--brand-blue)"/>
          <rect x="8" y="10.5" width="16" height="11" rx="1" fill="#fff"/>
          <polyline points="8.5,11 16,17 23.5,11" fill="none" stroke="var(--brand-blue)" stroke-width="1.5"/>
        </svg>
        <span>Torvane PT</span>
      </li>
    </ul>
  </div>
</body>
</html>
```